Brisk Valets Postcard - I would like to send this using MAIL to my prospects and current clients.

This store is under new management. I would like to design a high end postcard that showcases our services. Here is a list of the services that we provide to our customers.
- Premium Organic Dry Cleaning
- Laundered Shirts
- Expert Alterations
- Shoes and Leather Repairs by Tenby Partners
- Area Rug Cleaning by Harlow Launderers
- Leather and Suede Cleaning by Pike Launderers
- Household Items
- Wedding Dress Cleaning and Preservation
I would like to offer 10% off (one-time use) coupon as well as 20% off to new customers.
Here is a logo file with location details.
While designing postcards, I would like to showcase stack of different garments (Season based) and household items. Also, use the colors that I have provided in the logo design.
We also offer Free Pick up and delivery.
About Us:
Brisk Valets is a premium dry cleaning and garment care service dedicated to delivering exceptional quality, convenience, and personalized attention. Located in the heart of Bedminster, NJ, we specialize in eco-friendly dry cleaning, expert stain removal, professional garment pressing, and specialized care for delicate fabrics, designer clothing, household items, and formal wear.
Our mission is to provide reliable, high-quality service while preserving the longevity and appearance of our customers’ garments. With state-of-the-art equipment, experienced staff, and a commitment to customer satisfaction, Brisk Valets ensures your clothing looks and feels its best — every time.
We also offer convenient services such as same-day cleaning, alterations, wash & fold, and pickup and delivery options, making garment care simple and hassle-free for our busy clientele.
Experience the difference with Brisk Valets — where luxury care meets everyday convenience.

Target Market(s)

Household above $100K

Industry/Entity Type

Dry Cleaning

Font styles to use
Serif

Colors
0054AA
0677BA
7BADD7
CADEEF
E8F1F8
FFC000
F8CF3A
FAE287
FDF2CF
FEFAEE

Requirements
Must have
• Elegant Design with stacked clothes, highlight Organic Dry Cleaning store. The color schemes should have these colors. D4AF37 (Fonts), 0D1B2A (Background). These are used in my logo and tagline.
Nice to have
• On the backside I would like to show our location on the map, streets

```html
<!DOCTYPE html>
<html lang="en">
<head>
<meta charset="utf-8">
<title>Brisk Valets Postcard</title>
<link rel="stylesheet" href="https://fonts.googleapis.com/css2?family=Cinzel:wght@600;700&family=EB+Garamond:wght@400;500&display=swap">
<style>
  :root {
    --navy: #0d1b2a;
    --gold: #d4af37;
    --gold-band: #d4b035;
    --white: #ffffff;
    --paper: #ffffff;
    --backdrop: #dcdcdc;
    --rule: #333333;
  }
  * { margin: 0; padding: 0; box-sizing: border-box; }
  html, body { width: 891px; height: 1200px; overflow: hidden; }
  body { background: var(--backdrop); position: relative; font-family: "EB Garamond", serif; }

  .card { position: absolute; left: 106px; width: 678px; height: 461px; overflow: hidden; }
  .card-front { top: 120px; background: var(--navy); }
  .card-back { top: 618px; background: var(--paper); }

  .front-art { position: absolute; inset: 0; }

  .brand { position: absolute; left: 0; width: 283px; top: 92px; text-align: center; color: var(--gold); }
  .brand-name { font-family: "Cinzel", serif; font-weight: 700; font-size: 33px; line-height: 36px; letter-spacing: 1px; }
  .brand-tagline { font-size: 12px; margin-top: 4px; letter-spacing: 0.2px; }
  .brand-address { font-size: 12px; line-height: 16px; margin-top: 8px; }

  .headline { position: absolute; left: 40px; top: 266px; font-family: "Cinzel", serif; font-weight: 700;
    font-size: 41px; line-height: 44px; letter-spacing: 2px; color: var(--gold); }

  .offer-badge { position: absolute; left: 474px; top: 248px; width: 160px; height: 160px; }

  .services-panel { position: absolute; left: 0; top: 0; width: 339px; height: 374px; background: var(--navy); }
  .services-title { position: absolute; left: 40px; top: 36px; font-family: "Cinzel", serif; font-weight: 700;
    font-size: 24px; letter-spacing: 0.5px; color: var(--gold); }
  .services-list { position: absolute; left: 42px; top: 76px; list-style: none; color: var(--white); font-size: 11.5px; }
  .services-list li { height: 20.5px; line-height: 16px; padding-left: 11px; position: relative; }
  .services-list li::before { content: ""; position: absolute; left: 0; top: 5px; width: 5px; height: 5px;
    border-radius: 50%; background: var(--gold); }

  .garment-photo { position: absolute; top: 254px; width: 82px; height: 105px; border-radius: 2px; }
  .photo-suit { left: 40px; background: linear-gradient(90deg, #1b1b1b 0%, #e8e4df 35%, #1a1a1a 50%, #e8e4df 65%, #1b1b1b 100%); }
  .photo-stack { left: 139px; background: linear-gradient(180deg, #2c3f6b 0%, #3a5686 30%, #9aa9a0 50%, #5d7783 62%, #a3263c 80%, #6e1c3a 100%); }
  .photo-tees { left: 239px; background: linear-gradient(90deg, #f1d9b8 0%, #f6f3ee 25%, #0f5b3e 45%, #0f5b3e 60%, #f3f3f3 78%, #1d2127 100%); }

  .stamp-box { position: absolute; left: 528px; top: 45px; width: 105px; height: 105px; border: 1px solid var(--rule); }
  .address-rule { position: absolute; left: 353px; width: 280px; height: 1px; background: var(--rule); }

  .contact-band { position: absolute; left: 0; top: 374px; width: 678px; height: 87px; background: var(--gold-band); color: var(--white); }
  .contact-phone { position: absolute; left: 68px; top: 6px; font-family: "EB Garamond", serif; font-weight: 500;
    font-size: 25px; letter-spacing: 2.5px; }
  .contact-address { position: absolute; left: 68px; top: 38px; font-size: 11px; letter-spacing: 1px; }
  .icon { position: absolute; left: 40px; fill: var(--white); }
  .icon-phone { top: 10px; }
  .icon-pin { top: 39px; }
</style>
</head>
<body>

<section class="card card-front">
  <svg class="front-art" width="678" height="461" viewBox="0 0 678 461">
    <defs>
      <linearGradient id="rackTones" x1="0" y1="0" x2="1" y2="0">
        <stop offset="0" stop-color="#8d8d8f"/>
        <stop offset="0.35" stop-color="#b3b4b2"/>
        <stop offset="0.55" stop-color="#7d9580"/>
        <stop offset="0.8" stop-color="#6d8a72"/>
        <stop offset="1" stop-color="#b5502f"/>
      </linearGradient>
    </defs>
    <polygon role="img" aria-label="Photo of shirts in grey, sage green and rust hanging on wooden hangers"
      points="515,0 678,0 678,461 515,461 412,223" fill="url(#rackTones)"/>
    <polyline points="508,-4 405,223 508,465" fill="none" stroke="var(--gold)" stroke-width="12"/>
  </svg>

  <div class="brand">
    <div class="brand-name">BRISK<br>VALETS</div>
    <div class="brand-tagline">Luxury Care For Your Finest Wear</div>
    <div class="brand-address">48 Alder Crest Road<br>Fairmont, NJ 07999</div>
  </div>

  <h1 class="headline">ORGANIC<br>DRYCLEANING<br>STORE</h1>

  <svg class="offer-badge" viewBox="0 0 160 160">
    <circle cx="80" cy="80" r="80" fill="var(--gold)"/>
    <circle cx="80" cy="80" r="66" fill="none" stroke="var(--navy)" stroke-width="3"/>
    <text x="78" y="52" text-anchor="middle" font-family="EB Garamond, serif" font-size="16" fill="var(--navy)">OFFER</text>
    <text x="72" y="96" text-anchor="middle" font-family="EB Garamond, serif" font-weight="500" font-size="44" fill="var(--navy)">10%</text>
    <text transform="translate(130 80) rotate(-90)" text-anchor="middle" font-family="EB Garamond, serif" font-size="15" fill="var(--navy)">OFF</text>
    <text x="78" y="114" text-anchor="middle" font-family="EB Garamond, serif" font-size="10.5" fill="var(--navy)">(ONE-TIME USE)</text>
  </svg>
</section>

<section class="card card-back">
  <div class="services-panel">
    <h2 class="services-title">OUR SERVICES</h2>
    <ul class="services-list">
      <li>Premium Organic Dry Cleaning</li>
      <li>Laundered Shirts</li>
      <li>Expert Alterations</li>
      <li>Shoes and Leather Repairs by Tenby Partners</li>
      <li>Area Rug Cleaning by Harlow Launderers</li>
      <li>Leather and Suede Cleaning by Pike Launderers</li>
      <li>Household Items</li>
      <li>Wedding Dress Cleaning and Preservation</li>
    </ul>
    <div class="garment-photo photo-suit" role="img" aria-label="Photo of a dark suit with white shirt and black tie"></div>
    <div class="garment-photo photo-stack" role="img" aria-label="Photo of a stack of folded garments in navy, sage and burgundy"></div>
    <div class="garment-photo photo-tees" role="img" aria-label="Photo of t-shirts in white, green and black on wooden hangers"></div>
  </div>

  <div class="stamp-box"></div>
  <div class="address-rule" style="top:204px"></div>
  <div class="address-rule" style="top:249px"></div>
  <div class="address-rule" style="top:294px"></div>
  <div class="address-rule" style="top:338px"></div>

  <div class="contact-band">
    <svg class="icon icon-phone" width="14" height="14" viewBox="0 0 24 24">
      <path d="M6.6 10.8a15.5 15.5 0 0 0 6.6 6.6l2.2-2.2c.3-.3.7-.4 1-.2 1.1.4 2.3.6 3.6.6.6 0 1 .4 1 1V20c0 .6-.4 1-1 1A17 17 0 0 1 3 4c0-.6.4-1 1-1h3.5c.6 0 1 .4 1 1 0 1.3.2 2.5.6 3.6.1.3 0 .7-.2 1z"/>
    </svg>
    <div class="contact-phone">555-318-0472</div>
    <svg class="icon icon-pin" width="14" height="18" viewBox="0 0 24 30">
      <path d="M12 0C5.4 0 0 5.2 0 11.7 0 20 12 30 12 30s12-10 12-18.3C24 5.2 18.6 0 12 0zm0 16a4.5 4.5 0 1 1 0-9 4.5 4.5 0 0 1 0 9z"/>
    </svg>
    <div class="contact-address">210 Linden Court, Unit 5, Westbrook, NJ 08899</div>
  </div>
</section>

</body>
</html>
```